Brill Insurance Agency - Business Cards

Hello, I am needing new trendy business cards for our Insurance Agency now that I have a new Logo. I have attached our new logo with several color options along with a business card design that I like. I am leaning towards burgundy and blue colors. I have attached our current business card. I have also attached a headshot of our company president, Martin Vale, that you can use if you wish. Thank you so much in advance for all the wonderful designs!!!!

Target Market(s)

We want to look very professional to potential customers and we also want to look very professional so insurance companies will want to contract with us to sell their product.

Industry/Entity Type

Insurance

Contact Information for Business Card

Martin Vale
mvale@brillagency.com
Business: 555-213-4087
Fax: 555-213-7751
Cell: 555-390-2618
Toll Free: 888-555-0194
42 W Elm Rd Millbrook, KS 66012
www.brillagency.net

Font styles to use
Serif
Sans Serif

Colors
0355a3
3277b5
f04a50
ec1f27

Requirements
Nice to have
• I love creativity. The more creative and balanced a business card design the more I will like it. I would like the card to be printed horizontally instead of vertically.
Should not have
• My project should not have the Allied Coverage Network logo. It is no longer used in the industry.

```html
<!DOCTYPE html>
<html lang="en">
<head>
<meta charset="utf-8">
<title>Brill Insurance Agency – Business Cards</title>
<link href="https://fonts.googleapis.com/css2?family=Mulish:wght@400;600;700;800&display=swap" rel="stylesheet">
<style>
  :root {
    --brand-blue: #1e5486;
    --page-bg: #f2f2f2;
    --card-white: #ffffff;
    --ink: #333333;
    --muted: #9a9a9a;
    --accent-red: #e8211f;
  }
  * { margin: 0; padding: 0; box-sizing: border-box; }
  html, body { width: 1200px; height: 1000px; overflow: hidden; }
  body {
    position: relative;
    background: var(--page-bg);
    font-family: "Mulish", sans-serif;
  }
  .card {
    position: absolute;
    left: 261px;
    width: 679px;
    height: 387px;
    border-radius: 20px;
    overflow: hidden;
  }
  .card-front { top: 91px; background: var(--brand-blue); color: var(--card-white); }
  .card-back { top: 520px; background: var(--card-white); }

  .front-name {
    position: absolute; left: 33px; top: 170px; width: 250px;
    text-align: center; font-weight: 800; line-height: 1.1;
  }
  .front-name .line-main { display: block; font-size: 26px; }
  .front-name .line-sub { display: block; font-size: 15px; letter-spacing: 3px; margin-top: 2px; }
  .front-web { position: absolute; left: 87px; top: 321px; font-size: 17px; }
  .front-ring { position: absolute; left: 307px; top: 60px; }

  .back-lockup { position: absolute; left: 38px; top: 137px; display: flex; align-items: center; }
  .lockup-dot { width: 58px; height: 58px; border-radius: 50%; background: var(--brand-blue); }
  .lockup-divider { width: 1.5px; height: 72px; background: var(--ink); margin: 0 9px 0 26px; }
  .lockup-name { color: var(--brand-blue); font-weight: 800; line-height: 1.1; }
  .lockup-name .line-main { display: block; font-size: 20px; }
  .lockup-name .line-sub { display: block; font-size: 12px; letter-spacing: 3px; margin-top: 3px; }
  .toll-free { font-size: 16px; color: var(--ink); margin-top: 8px; }
  .toll-free .label { color: var(--accent-red); }

  .contact { position: absolute; left: 378px; top: 73px; }
  .person-name { font-size: 24px; font-weight: 800; color: var(--brand-blue); }
  .person-title { font-size: 17px; color: var(--muted); margin-top: -2px; }
  .contact-row { display: flex; align-items: center; margin-top: 14px; }
  .contact-row:first-of-type { margin-top: 14px; }
  .contact-icon { width: 27px; height: 27px; margin-right: 12px; flex: none; }
  .contact-lines { font-size: 17px; color: var(--ink); line-height: 1.25; }
  .contact-lines .note { color: var(--muted); }

  .address-band {
    position: absolute; left: 0; top: 331px; width: 100%; height: 32px;
    background: var(--brand-blue); color: var(--card-white);
    font-size: 18px; text-align: center; line-height: 32px;
  }
</style>
</head>
<body>
  <section class="card card-front">
    <div class="front-name">
      <span class="line-main">BRILL INSURANCE</span>
      <span class="line-sub">AGENCY INC</span>
    </div>
    <div class="front-web">www.brillagency.net</div>
    <svg class="front-ring" width="270" height="270" viewBox="0 0 270 270" aria-hidden="true">
      <circle cx="135" cy="135" r="124" fill="none" stroke="#ffffff" stroke-width="20"/>
    </svg>
  </section>

  <section class="card card-back">
    <div class="back-lockup">
      <div class="lockup-dot"></div>
      <div class="lockup-divider"></div>
      <div>
        <div class="lockup-name">
          <span class="line-main">BRILL INSURANCE</span>
          <span class="line-sub">AGENCY INC</span>
        </div>
        <div class="toll-free"><span class="label">Toll Free</span> : 888-555-0194</div>
      </div>
    </div>

    <div class="contact">
      <div class="person-name">Martin Vale</div>
      <div class="person-title">Owner | CEO</div>

      <div class="contact-row">
        <svg class="contact-icon" viewBox="0 0 28 28" aria-hidden="true">
          <circle cx="14" cy="14" r="14" fill="var(--brand-blue)"/>
          <path d="M9.5 7.5l3 0.2 1 3.3-1.8 1.3a9 9 0 0 0 4 4l1.3-1.8 3.3 1 .2 3c-.5 1-1.6 1.5-2.7 1.3A12 12 0 0 1 8.2 10.2c-.2-1.1.3-2.2 1.3-2.7z" fill="#fff"/>
        </svg>
        <div class="contact-lines">
          555 - 213 - 4087 <span class="note">(Business)</span><br>
          555 - 390 - 2618 <span class="note">(Cell)</span>
        </div>
      </div>

      <div class="contact-row">
        <svg class="contact-icon" viewBox="0 0 28 28" aria-hidden="true">
          <circle cx="14" cy="14" r="14" fill="var(--brand-blue)"/>
          <rect x="8" y="9" width="3" height="11" fill="#fff"/>
          <rect x="12" y="9" width="8" height="11" rx="1" fill="#fff"/>
          <rect x="13.5" y="7" width="5" height="3" fill="#fff"/>
          <rect x="14" y="12" width="4" height="1.5" fill="var(--brand-blue)"/>
          <rect x="14" y="15" width="4" height="1.5" fill="var(--brand-blue)"/>
        </svg>
        <div class="contact-lines">555 - 213 - 7751</div>
      </div>

      <div class="contact-row">
        <svg class="contact-icon" viewBox="0 0 28 28" aria-hidden="true">
          <circle cx="14" cy="14" r="14" fill="var(--brand-blue)"/>
          <g fill="none" stroke="#fff" stroke-width="1.4">
            <circle cx="14" cy="14" r="7"/>
            <ellipse cx="14" cy="14" rx="3" ry="7"/>
            <line x1="7" y1="14" x2="21" y2="14"/>
          </g>
        </svg>
        <div class="contact-lines">
          mvale@brillagency.com<br>
          www.brillagency.net
        </div>
      </div>
    </div>

    <div class="address-band">42 W Elm Rd Millbrook, KS 66012</div>
  </section>
</body>
</html>
```